New and upgraded www.valmorefunds.com content & design financial markets

We need an upgrade of our site. The current site is www.valmorefunds.com
Navigation with full site map i.e. the user can select any page from any menu item.

The “Insights” (Insikter) page will remain as is except new design AND with far more possibilities to add thumbnails, picts, videos etc. The user will have to logon to be able to read the full story.

The “Produkter & Tjänster” (“How to invest” in current web) will contain about the same info as the current “How to invest” pages.

Some pages will contain one or more videos and or speaker supported “live” graphics which we will supply. The media content shall be easy to change.

The site will have two languages from start, English and Swedish. There will be more languages added within 1 year or slightly more.

All texts will be provided by us.

I’m attaching a PDF with suggested content for some of the new pages. However this is just content and absolutely no design. We need new design for the total of the site as well as for the graphics.

Expectation info:
These sites (Both major players in our business) can be used as inspiration:
https://www.tessandrik.com/eu/en/
https://www.bravelholm.com/index.html

Below some opt-OUT and opt-IN graphic rules in connection with the Web supporting our business acumen and brand:

Opt-OUT:
- images similar to educational comic books - it signals an authoritarian approach where the customer is small (insubstantial).
- images that signal trading, cyber, mystery and fast-paced business. We are extremely long-term and invest in real companies
- avoid images containing coins, calculators and banknotes. We're not a savings bank company. or payment service-branch
- avoid images of large data flows, because we should not make facts complex, but simple and comprehensible
- avoid sensing pictures of photo models. We are real people who stand for our efforts. We're not going to hide.
- avoid pictures of suits and tie. They signal rigid-banking. We're smart-investment, flexible, adaptable. Rather curl up your sleeves and show that we’re building something valuable.
- avoid pictures of skyscrapers and cool bank pictures - because they signal the more old valuations of big capital and giant banks - that we are not at all. I know we've had clean facades before. As long as we're not talking about bank skyscrapers, I'm in.

Opt-IN
- pictures of Tomas in moderate amount - he is our symbol person
- films with Tomas and explaining graphical films - explaining and clarifying
- images of pedagogy that give the customer a sense of overview and insights that we give to the customers in our service
- illustrations that explain and deepen our work
- pictures and bars that in 3d illustrate our consistent results and stable delivery
- images that signal that we have a full grasp of data, flows and analyses - without the image becoming a space adventure
- use the logo as a grid, shape and colour.
- no genre portraits, rather pictures of real customers - which gives a sense of why they are customers here
- images that support our core i.e. is science, innovation, unrestricted thinking (“out of the box” – (don’t like that sentence)), smart-solutions, data-driven, client-cantered, flexible and adaptable to client needs and expectation.
- Solid - to be trustworthy in any economic climate
- Long term - consistent work and choices. No trading. Numbers talk
- Data-driven - real tech - combining years of work in finance with straight on tech

Presenting on the webpage:
The story in text and illustration
Show the truth - we have a great history to show and give space
Only numbers and graphs that has a meaning - no artificial numbers etc.

Target Market(s)

Europe

Coding

Coded - Design and coding required

Number of Pages Required

5+ page

Colors

Designer to choose colors to be used in the design.

Requirements
Must have
• Colours in line with www.valmorefunds.com

```html
<!DOCTYPE html>
<html lang="en">
<head>
<meta charset="utf-8">
<title>Valmore Funds — Your Personal Investment Advisor</title>
<link href="https://fonts.googleapis.com/css2?family=Poppins:wght@300;400;500;600;700&display=swap" rel="stylesheet">
<style>
:root{
  --navy:#0c176a;
  --navy-deep:#0a1259;
  --blue:#1c3aa9;
  --royal:#2f4fd0;
  --periwinkle:#7b8cf2;
  --lavender:#e6e9fd;
  --mist:#f5f5f7;
  --ink:#2b2b3a;
  --text:#4a4a58;
  --white:#ffffff;
}
*{box-sizing:border-box;margin:0;padding:0}
html,body{width:1200px;height:4071px;overflow:hidden;background:var(--white)}
body{font-family:'Poppins',sans-serif;color:var(--ink)}
.page{position:relative;width:1200px;height:4071px;overflow:hidden;background:var(--white)}
.abs{position:absolute}
.brand{display:flex;align-items:center;gap:12px;font-family:'Poppins',sans-serif;font-weight:400;color:var(--navy);white-space:nowrap}
.brand-square{width:28px;height:28px;background:var(--navy)}
.btn{position:absolute;display:flex;align-items:center;justify-content:center;border-radius:40px;
  background:linear-gradient(90deg,var(--blue),var(--navy-deep));color:var(--white);font-weight:600;
  box-shadow:0 6px 14px rgba(12,23,106,.35);letter-spacing:.2px;white-space:nowrap;text-decoration:none}
.ph{position:absolute}
/* header */
.site-header .brand{left:111px;top:24px;font-size:38px}
.nav{position:absolute;left:536px;top:34px;display:flex;gap:2px;font-size:14px;font-weight:500;color:var(--white);white-space:nowrap}
.nav a{color:var(--white);text-decoration:none;padding:4px 8px;white-space:nowrap}
.nav a.active{border:1.5px solid var(--white);border-radius:20px}
/* hero */
.hero-kicker{left:111px;top:256px;font-size:30px;font-weight:400;color:var(--navy)}
.hero-title{left:111px;top:296px;font-size:36px;font-weight:700;color:var(--blue);letter-spacing:1.5px;white-space:nowrap}
.hero-sub{left:111px;top:368px;width:445px;font-size:15px;line-height:24px;font-weight:500;color:var(--ink)}
/* section heads */
.sec-head{position:absolute;display:flex;align-items:center;gap:10px;color:var(--navy);font-size:33px;font-weight:400;white-space:nowrap}
.sec-head.center{left:0;width:1200px;justify-content:center}
.sec-head .mark{width:26px;height:26px;background:var(--navy)}
.sec-head .bar{width:2px;height:36px;background:var(--navy)}
.sec-head b{font-weight:700;color:var(--blue)}
/* about */
.about-text{left:588px;top:946px;width:500px;font-size:13.2px;line-height:22px;color:var(--text)}
.about-text p+p{margin-top:10px}
/* features */
.features-bg{left:0;top:1470px;width:1200px;height:596px;background:var(--mist)}
.feature{position:absolute;top:1696px;width:300px;height:260px}
.feature svg{position:absolute;left:0;top:0}
.feature-body{position:absolute;left:70px;top:140px;width:228px;text-align:center;color:var(--white)}
.feature-body h3{font-size:16px;font-weight:600;margin-bottom:6px;white-space:nowrap}
.feature-body p{font-size:12px;line-height:17px;padding:0 28px}
/* philosophy */
.phil-kicker{left:186px;top:2240px;font-size:20px;color:var(--navy);white-space:nowrap}
.phil-title{left:186px;top:2266px;font-size:32px;font-weight:700;color:var(--blue);letter-spacing:1px;white-space:nowrap}
.phil-mark{left:111px;top:2247px;width:44px;height:44px;background:var(--navy)}
.phil-bar{left:170px;top:2240px;width:2px;height:64px;background:var(--navy)}
.phil-list{left:111px;top:2335px;width:560px;list-style:none;font-size:15px;line-height:32.6px;color:var(--text)}
.phil-list li{position:relative;padding-left:24px}
.phil-list li::before{content:"";position:absolute;left:0;top:12px;width:11px;height:11px;background:var(--navy)}
/* what we do */
.wwd-bg{left:0;top:2846px;width:1200px;height:900px;background:var(--mist)}
.card{position:absolute;top:3083px;width:294px;height:427px;background:var(--white);border-radius:34px;
  box-shadow:0 10px 24px rgba(20,30,90,.12);overflow:hidden;text-align:center}
.card .photo{position:absolute;left:0;top:0;width:294px;height:195px}
.card .wave{position:absolute;left:0;top:140px}
.card h3{position:absolute;left:0;right:0;top:226px;font-size:19px;font-weight:600;color:var(--navy);white-space:nowrap}
.card p{position:absolute;left:22px;right:22px;top:266px;font-size:13.5px;line-height:24px;color:var(--text)}
.card .btn{left:93px;top:356px;width:108px;height:42px;font-size:12.5px}
/* footer */
.footer .brand{left:454px;top:3800px;font-size:40px;color:var(--white)}
.footer .brand-square{background:var(--white);width:30px;height:30px}
.contacts{position:absolute;left:205px;top:3906px;display:flex;align-items:center;gap:26px;color:var(--white);font-size:17px;font-weight:500;white-space:nowrap}
.contact{display:flex;align-items:center;gap:12px}
.contact .ico{width:44px;height:44px;border:2px solid var(--white);border-radius:50%;display:flex;align-items:center;justify-content:center}
.contact.addr span{font-size:15px;line-height:24px}
.footer-rule{left:108px;top:4002px;width:978px;height:1px;background:rgba(255,255,255,.45)}
.copyright{left:0;top:4026px;width:1200px;text-align:center;color:var(--white);font-size:15px;font-weight:500}
</style>
</head>
<body>
<div class="page">

  <svg class="abs" style="left:0;top:0" width="1200" height="680" viewBox="0 0 1200 680" aria-hidden="true">
    <path d="M470 0 C500 140 640 170 700 260 C760 360 860 470 980 560 C1060 620 1150 660 1200 660 L1200 0 Z" fill="#eef0fd"/>
    <path d="M500 0 C530 120 660 150 720 240 C780 340 880 440 990 525 C1070 590 1150 630 1200 640 L1200 0 Z" fill="#a9b4f7"/>
    <path d="M540 0 C570 110 690 140 750 220 C810 310 900 410 1010 490 C1080 545 1150 585 1200 600 L1200 0 Z" fill="#6f80ef"/>
    <path d="M590 0 C630 100 730 120 790 190 C850 270 930 370 1030 440 C1100 490 1160 520 1200 530 L1200 0 Z" fill="#3f55d6"/>
    <path d="M650 0 C700 80 780 100 840 160 C900 230 970 320 1060 380 C1120 420 1170 440 1200 445 L1200 0 Z" fill="#3544bf"/>
  </svg>
  <div class="ph" role="img" aria-label="Isometric illustration of advisors around 3D bar and pie charts on a platform" style="left:585px;top:142px;width:585px;height:443px;border-radius:40px;background:linear-gradient(135deg,#f2f3fb 0%,#dfe3fb 55%,#f6b7a0 100%);opacity:.92"></div>

  <header class="site-header">
    <div class="abs brand"><span class="brand-square"></span>Valmore Funds</div>
    <nav class="nav">
      <a class="active" href="#">Home</a><a href="#">Philosophy</a><a href="#">How To Invest</a><a href="#">What We Do</a><a href="#">Contact</a><a href="#">Insights</a><a href="#">Login</a>
    </nav>
  </header>

  <section class="hero">
    <div class="abs hero-kicker">Your Personal</div>
    <h1 class="abs hero-title">INVESTMENT ADVISOR</h1>
    <p class="abs hero-sub">Valmore Funds is Your Global Reference for Investment Advice</p>
    <a class="btn" style="left:111px;top:446px;width:194px;height:60px;font-size:18px">GET STARTED</a>
  </section>

  <svg class="abs" style="left:0;top:630px" width="520" height="690" viewBox="0 0 520 690" aria-hidden="true">
    <path d="M0 10 C120 -20 260 40 340 130 C420 220 520 300 500 420 C480 560 330 640 180 670 C110 685 40 690 0 680 Z" fill="#eef0fd"/>
    <path d="M0 55 C120 30 250 80 320 160 C390 240 470 320 450 430 C430 540 310 610 180 630 C110 640 40 640 0 630 Z" fill="#7b8cf2"/>
    <path d="M0 90 C120 70 240 115 300 185 C360 255 430 330 410 430 C390 525 290 585 170 600 C100 608 40 606 0 600 Z" fill="#1c3aa9"/>
    <path d="M0 120 C110 105 220 145 275 205 C330 265 390 335 372 425 C354 510 265 560 160 572 C95 578 40 576 0 572 Z" fill="#0c176a"/>
  </svg>
  <div class="ph" role="img" aria-label="Illustration of an analyst at a laptop and a presenter beside a rising line chart" style="left:40px;top:840px;width:440px;height:370px;border-radius:120px 160px 140px 120px;background:linear-gradient(140deg,#e8f1ff 0%,#cfe3ff 60%,#9fc0f5 100%)"></div>

  <div class="sec-head" style="left:588px;top:884px"><span class="mark"></span><span class="bar"></span><span>ABOUT <b>VALMORE FUNDS</b></span></div>
  <div class="abs about-text">
    <p>We are a privately held firm dedicated to clients who have entrusted us with their wealth. We act solely and transparently in the best interest of our clients. We pride ourselves on our discretion and confidentiality.</p>
    <p>You can be assured of a totally Client-centric service, high quality, totally unbiased, investment advice. We are fee only based, i.e. we have no affiliations with any financial institutions – we do not take any commission from any investment product provider – We Work Only for You!</p>
  </div>
  <a class="btn" style="left:588px;top:1141px;width:124px;height:56px;font-size:14px">READ MORE</a>

  <div class="abs features-bg"></div>
  <svg class="abs" style="left:0;top:1370px" width="1200" height="130" viewBox="0 0 1200 130" aria-hidden="true">
    <path d="M0 80 C200 20 420 20 620 60 C800 95 960 10 1200 20 L1200 130 L0 130 Z" fill="#dfe6f7"/>
    <path d="M0 95 C220 50 420 40 640 80 C820 110 980 70 1200 75 L1200 130 L0 130 Z" fill="#f5f5f7"/>
    <path d="M350 110 C480 70 620 60 760 100 C660 110 520 120 350 110 Z" fill="#1c3aa9"/>
    <path d="M0 72 L30 92 L0 100 Z" fill="#1c3aa9"/>
    <path d="M1200 50 L1165 78 L1200 95 Z" fill="#1c3aa9"/>
  </svg>
  <div class="sec-head center" style="top:1578px"><span class="mark"></span><span class="bar"></span><span>VALMORE <b>FEATURES</b></span></div>

  <div class="feature" style="left:100px">
    <svg width="320" height="270" viewBox="0 0 320 270" aria-hidden="true">
      <text x="0" y="210" font-family="Poppins,sans-serif" font-size="230" font-weight="300" fill="none" stroke="#0c176a" stroke-width="2">1</text>
      <circle cx="185" cy="130" r="128" fill="#f5f5f7" stroke="#0c176a" stroke-width="2.5"/>
      <circle cx="86" cy="48" r="5" fill="#0c176a"/>
      <path d="M71 130 A114 114 0 0 1 299 130 Z" fill="#ffffff"/>
      <path d="M71 130 A114 114 0 0 0 299 130 Z" fill="#0c176a"/>
      <circle cx="185" cy="70" r="28" fill="none" stroke="#0c176a" stroke-width="3"/>
      <path d="M176 63 a9 9 0 1 1 12 8 c-3 2 -3 4 -3 8" fill="none" stroke="#0c176a" stroke-width="3.5" stroke-linecap="round"/>
      <circle cx="185" cy="86" r="2.5" fill="#0c176a"/>
    </svg>
    <div class="feature-body" style="left:71px"><h3>Why Choose Us</h3><p>We secure your interests by continuously keeping your Investment</p></div>
  </div>

  <div class="feature" style="left:439px">
    <svg width="320" height="270" viewBox="0 0 320 270" aria-hidden="true">
      <text x="0" y="210" font-family="Poppins,sans-serif" font-size="230" font-weight="300" fill="none" stroke="#0c176a" stroke-width="2">2</text>
      <circle cx="185" cy="130" r="128" fill="#f5f5f7" stroke="#0c176a" stroke-width="2.5"/>
      <circle cx="86" cy="48" r="5" fill="#0c176a"/>
      <path d="M71 130 A114 114 0 0 1 299 130 Z" fill="#ffffff"/>
      <path d="M71 130 A114 114 0 0 0 299 130 Z" fill="#0c176a"/>
      <circle cx="185" cy="64" r="17" fill="none" stroke="#0c176a" stroke-width="2.5"/>
      <text x="185" y="71" text-anchor="middle" font-family="Poppins,sans-serif" font-size="18" font-weight="600" fill="#0c176a">$</text>
      <path d="M158 96 h12 l10 -6 h18 M158 86 v20" fill="none" stroke="#0c176a" stroke-width="2.5" stroke-linecap="round"/>
      <path d="M165 40 v14 M205 40 v14" stroke="#0c176a" stroke-width="2.5" stroke-linecap="round"/>
    </svg>
    <div class="feature-body" style="left:71px"><h3>Investment Intelligence</h3><p>We secure your interests by continuously keeping your Investment</p></div>
  </div>

  <div class="feature" style="left:775px">
    <svg width="320" height="270" viewBox="0 0 320 270" aria-hidden="true">
      <text x="0" y="210" font-family="Poppins,sans-serif" font-size="230" font-weight="300" fill="none" stroke="#0c176a" stroke-width="2">3</text>
      <circle cx="185" cy="130" r="128" fill="#f5f5f7" stroke="#0c176a" stroke-width="2.5"/>
      <circle cx="86" cy="48" r="5" fill="#0c176a"/>
      <path d="M71 130 A114 114 0 0 1 299 130 Z" fill="#ffffff"/>
      <path d="M71 130 A114 114 0 0 0 299 130 Z" fill="#0c176a"/>
      <circle cx="183" cy="60" r="13" fill="none" stroke="#0c176a" stroke-width="2.5"/>
      <path d="M160 98 c0 -14 10 -22 23 -22 s23 8 23 22 Z" fill="none" stroke="#0c176a" stroke-width="2.5"/>
      <text x="213" y="98" font-family="Poppins,sans-serif" font-size="18" font-weight="600" fill="#0c176a">$</text>
    </svg>
    <div class="feature-body" style="left:71px"><h3>Client Focus</h3><p>We secure your interests by continuously keeping your Investment</p></div>
  </div>

  <svg class="abs" style="left:640px;top:2100px" width="560" height="690" viewBox="0 0 560 690" aria-hidden="true">
    <path d="M560 0 C500 40 440 90 330 110 C200 135 120 200 110 300 C100 420 190 520 320 600 C410 655 500 680 560 685 Z" fill="#eef0fd"/>
    <path d="M560 40 C500 80 440 120 340 140 C220 165 150 225 145 310 C140 420 220 510 340 575 C420 620 500 640 560 645 Z" fill="#7b8cf2"/>
    <path d="M560 80 C500 115 440 150 350 170 C240 195 180 250 178 325 C176 420 250 495 355 550 C430 588 500 600 560 605 Z" fill="#1c3aa9"/>
    <path d="M560 120 C505 150 450 180 365 200 C265 225 215 270 214 340 C213 420 278 485 370 525 C440 555 505 565 560 568 Z" fill="#0c176a"/>
  </svg>
  <div class="ph" role="img" aria-label="Illustration of analysts around a large monitor showing charts under a magnifying glass" style="left:672px;top:2270px;width:440px;height:440px;border-radius:24px;background:linear-gradient(135deg,#f3f6ff 0%,#cdd9fb 55%,#8fd3e6 100%)"></div>

  <div class="abs phil-mark"></div>
  <div class="abs phil-bar"></div>
  <div class="abs phil-kicker">VALMORE INVESTMENT</div>
  <h2 class="abs phil-title">ADVISORY PHILOSOPHY</h2>
  <ul class="abs phil-list">
    <li>Systematic Adaption to Market Climate</li>
    <li>Attractive Risk Returns with Low Portfolio Turnover</li>
    <li>Europe and U.S. Investment Area</li>
    <li>Built to Follow or Outperform the Market During Upturns and Avoid Large Declines During Long – Term Market Turndowns</li>
    <li>Continuously Monitoring, Identifying and Implementing to Maintain</li>
    <li>Optimal Portfolio</li>
    <li>Long – Term Investment Strategy</li>
  </ul>
  <a class="btn" style="left:111px;top:2621px;width:122px;height:54px;font-size:14px">READ MORE</a>

  <div class="abs wwd-bg"></div>
  <svg class="abs" style="left:0;top:2800px" width="1200" height="80" viewBox="0 0 1200 80" aria-hidden="true">
    <path d="M0 45 C180 10 360 70 560 40 C760 10 960 55 1200 25 L1200 80 L0 80 Z" fill="#f5f5f7"/>
  </svg>
  <div class="sec-head center" style="top:2998px"><span class="mark"></span><span class="bar"></span><span>WHAT <b>WE DO</b></span></div>

  <article class="card" style="left:111px">
    <div class="photo" role="img" aria-label="Photo of a hand placing a coin on stacked coins beside a glass jar" style="background:linear-gradient(135deg,#f3e6d8 0%,#b99877 55%,#4b3a2c 100%)"></div>
    <svg class="wave" width="294" height="60" viewBox="0 0 294 60" aria-hidden="true"><path d="M0 30 C50 0 90 60 150 35 C210 10 250 20 294 30 L294 60 L0 60 Z" fill="#fff"/></svg>
    <h3>INVESTMENT INTELLIGENCE</h3>
    <p>We attempt to design attractive long term return portfolios, with low portfolio turnover,</p>
    <a class="btn">READ MORE</a>
  </article>
  <article class="card" style="left:454px">
    <div class="photo" role="img" aria-label="Photo of a tablet showing financial charts beside a coffee cup" style="background:linear-gradient(135deg,#eef1f6 0%,#b9c2d2 55%,#5a6275 100%)"></div>
    <svg class="wave" width="294" height="60" viewBox="0 0 294 60" aria-hidden="true"><path d="M0 30 C50 0 90 60 150 35 C210 10 250 20 294 30 L294 60 L0 60 Z" fill="#fff"/></svg>
    <h3>CLIENT FOCUS</h3>
    <p>Client is a real human being who has intentions and ambitions for his portfolio</p>
    <a class="btn">READ MORE</a>
  </article>
  <article class="card" style="left:795px">
    <div class="photo" role="img" aria-label="Photo of a magnifying glass over small model houses" style="background:linear-gradient(135deg,#4fb8c2 0%,#9fb7bd 55%,#5d5146 100%)"></div>
    <svg class="wave" width="294" height="60" viewBox="0 0 294 60" aria-hidden="true"><path d="M0 30 C50 0 90 60 150 35 C210 10 250 20 294 30 L294 60 L0 60 Z" fill="#fff"/></svg>
    <h3>INVESTMENT STRATEGY</h3>
    <p>We attempt to design attractive long term return portfolios, with low portfolio turnover,</p>
    <a class="btn">READ MORE</a>
  </article>

  <footer class="footer">
    <svg class="abs" style="left:0;top:3600px" width="1200" height="471" viewBox="0 0 1200 471" aria-hidden="true">
      <path d="M0 20 C200 90 420 20 620 60 C820 100 1000 10 1200 30 L1200 471 L0 471 Z" fill="#b7c3ec"/>
      <path d="M0 60 C220 110 430 40 640 80 C840 118 1010 50 1200 70 L1200 471 L0 471 Z" fill="#6f84d6"/>
      <path d="M0 75 C240 40 460 120 680 90 C880 62 1040 110 1200 85 L1200 471 L0 471 Z" fill="#0c176a"/>
    </svg>
    <div class="abs brand"><span class="brand-square"></span>Valmore Funds</div>
    <div class="contacts">
      <div class="contact">
        <span class="ico"><svg width="22" height="16" viewBox="0 0 22 16" aria-hidden="true"><rect x="1" y="1" width="20" height="14" rx="2" fill="none" stroke="#fff" stroke-width="1.8"/><path d="M1 2 L11 9 L21 2" fill="none" stroke="#fff" stroke-width="1.8"/></svg></span>
        <span>info@valmorefunds.com</span>
      </div>
      <div class="contact">
        <span class="ico"><svg width="20" height="20" viewBox="0 0 24 24" aria-hidden="true"><path d="M6 3 l3 0 l2 5 l-2 2 c1 3 3 5 6 6 l2 -2 l5 2 l0 3 c0 2 -2 3 -4 3 C10 21 3 14 3 7 C3 5 4 3 6 3 Z" fill="none" stroke="#fff" stroke-width="1.8" stroke-linejoin="round"/></svg></span>
        <span>Tel: +356 2140 7788</span>
      </div>
      <div class="contact addr">
        <span class="ico"><svg width="18" height="22" viewBox="0 0 18 22" aria-hidden="true"><path d="M9 21 C4 14 2 11 2 8 a7 7 0 0 1 14 0 c0 3 -2 6 -7 13 Z" fill="none" stroke="#fff" stroke-width="1.8"/><circle cx="9" cy="8" r="2.6" fill="none" stroke="#fff" stroke-width="1.8"/></svg></span>
        <span>12, Harbour Lane, SLM 2204<br>Sliema Malta</span>
      </div>
    </div>
    <div class="abs footer-rule"></div>
    <div class="abs copyright">Copyrights @ 2019 Valmore Funds. All Rights Reserved.</div>
  </footer>

</div>
</body>
</html>
```